LOS PINARES DE ORO - EXCLUSIVE AND LUXURY REAL ESTATE PROJECT

Se trata del diseño de un mono poste grande (4 m x 2 m) o (8m x 3m) anunciando la construcción de 30 villas de lujo en un terreno en primera línea de playa en el sur de España (Cádiz).

La idea es crear expectación y transmitir lujo y exclusividad.

Target Market(s)

Clientes de alto poder adquisitivo que quieran adquirir su segunda vivienda en un entorno privilegiado a escasos pasos de una de las playas más bonitas de Cádiz.

Industry/Entity Type

REAL ESTATE

Colors

Designer to choose colors to be used in the design.

Requirements
Must have
• LOS PINARES DE ORO as the name of the development
Nice to have
• Crear expectación con ideas del tipo: “Coming soon” o “No te lo puedes perder”

```html
<!DOCTYPE html>
<html lang="es">
<head>
<meta charset="utf-8">
<title>Los Pinares de Oro — Próximamente</title>
<link rel="stylesheet" href="https://fonts.googleapis.com/css2?family=IM+Fell+English+SC&family=Pinyon+Script&display=swap">
<style>
  :root {
    --bg-deep-teal: #112d36;
    --ink-white: #ffffff;
  }
  html, body {
    margin: 0;
    padding: 0;
    width: 1200px;
    height: 450px;
    overflow: hidden;
    background: var(--bg-deep-teal);
  }
  .billboard {
    position: relative;
    width: 1200px;
    height: 450px;
    background: var(--bg-deep-teal);
    color: var(--ink-white);
  }
  .billboard__line {
    position: absolute;
    left: 0;
    right: 0;
    margin: 0;
    text-align: center;
    white-space: nowrap;
    font-weight: 400;
  }
  .teaser {
    top: 88px;
    font-family: "IM Fell English SC", serif;
    font-size: 29px;
    line-height: 1;
    letter-spacing: 0.17em;
    text-indent: 0.17em;
  }
  .coming-soon {
    top: 143px;
    font-family: "IM Fell English SC", serif;
    font-size: 17px;
    line-height: 1;
    letter-spacing: 0.12em;
    text-indent: 0.12em;
  }
  .development-name {
    top: 178px;
    font-family: "Pinyon Script", cursive;
    font-size: 84px;
    line-height: 1.2;
  }
  .offer {
    top: 326px;
    font-family: "IM Fell English SC", serif;
    font-size: 27px;
    line-height: 1;
    letter-spacing: 0.02em;
  }
</style>
</head>
<body>
  <main class="billboard">
    <p class="billboard__line teaser">A veces es ahora o nunca…</p>
    <p class="billboard__line coming-soon">Próximamente:</p>
    <h1 class="billboard__line development-name">Los Pinares de Oro</h1>
    <p class="billboard__line offer">30 villas exclusivas frente al mar</p>
  </main>
</body>
</html>
```